依頼詳細
「仙台箪笥」は本来すべてが「手しごと」で作られたものを言います。しかし、近年は工場の機械で大量生産されたものを「仙台箪笥」として販売する企業が増えてきており、「本物」を作る職人達は価格競争で負けてしまいます。そんな中でも、柴崎庵では全ての工程を手しごとで行い、愚直に仙台箪笥を作り続けてきました。今のまま「安かろう、良かろう」の精神で仙台箪笥を販売する企業や、それを購入する消費者が増え続けてしまっては、江戸時代から培われてきた仙台の伝統が途絶えてしまいます。本チラシのデザインでは、そんな時代に警笛を鳴らすようなメッセージを込めて頂きたいと考えております。柴崎庵の代表・柴崎守氏からのメッセージや仙台箪笥の歴史を説明する資料を添付します。そちらを参考に、本物の箪笥の価値を伝えるデザインをして下さった方を採用とさせて頂きます。柴崎氏からの要望は2つあり、「『ずいぶんお堅い感じね』と言われるようなもの』」「伝統工芸をずっと続けてやっているんだなというイメージ」を意識してほしいとのことです。その他、何か質問があればどうぞお気軽にお問い合わせくださいませ。Mail→tokoharuwen@mailbox-demo.jp
記載項目
工房名/仙台箪笥 柴崎庵
住所/添付資料
電話番号/添付資料
ホームページURL・QRコード/現在HPリニューアル中のため、リニューアル完了後にこちらで入れ込みます。入れるスペースを分かるようにしておいてください。
キャッチコピー/デザインに合わせ、「依頼詳細」にある説明を参考に、心に刺さるコピーを入れてください。
写真/添付資料にある、柴崎守氏の写真と仙台箪笥の写真を中心に上手く組み合わせてデザインしてください。

〜コピー参考例〜
(コピーが浮かばなかった場合は、こちらのコピーの中から選んで入れてください。)

・一〇〇年先に繋ぎたい、一〇〇年前の財産
・本物しか作らない、「手しごと」の心
サイズ
A4
ページ数
片面
希望イメージ
シンプル 複雑
単色 カラフル
暗い 明るい
日常 高級
遊び心 厳粛
未来的 伝統的
女性的 男性的
希望する色
仙台箪笥の色にあった色を基調としてください。
納品ファイル
• イラストレーター形式 (.ai)
補足説明
現在リニューアル中ですが、こちらが現在の「柴崎庵」のホームページです。
http://homepage5.example-host.jp/shibasakian/
→ページ左上にあるロゴを使用できれば、デザインの中に入れ込んでほしいです
参考映像
https://www.videoshare-demo.jp/watch?v=Qw3rTz8LmNp
https://www.videoshare-demo.jp/watch?v=Vb6yHs2KoRd

柴崎氏ご本人に選んで頂きました。

この度は多数のご応募、誠にありがとうございました。どの作品も素晴らしいもので、一つに選ぶのが非常に難しかったです。またの機会にも、どうぞご応募頂ければ幸いです。宜しくお願い致します。

```html
<!DOCTYPE html>
<html lang="ja">
<head>
<meta charset="UTF-8">
<title>伝承の技、仙台箪笥 ｜ 仙台箪笥 柴崎庵</title>
<link rel="stylesheet" href="https://fonts.googleapis.com/css2?family=Shippori+Mincho+B1:wght@500;800&family=Noto+Serif+JP:wght@400;600&display=swap">
<style>
  :root{
    --lacquer-deep:#2a0507;
    --lacquer:#4a0d10;
    --lacquer-glow:#6e1a1c;
    --ink:#0b0606;
    --paper:#f4eee6;
    --paper-soft:#d9cfc4;
    --wood-light:#9a7a5e;
    --wood-dark:#3b2a22;
  }
  *{margin:0;padding:0;box-sizing:border-box}
  html,body{width:849px;height:1200px;overflow:hidden;background:var(--ink)}
  .flyer{
    position:relative;width:849px;height:1200px;overflow:hidden;
    background:
      repeating-linear-gradient(90deg,rgba(0,0,0,.10) 0 2px,transparent 2px 9px),
      radial-gradient(ellipse at 30% 25%,var(--lacquer-glow) 0%,var(--lacquer) 40%,var(--lacquer-deep) 75%,var(--ink) 100%);
    color:var(--paper);
    font-family:"Noto Serif JP",serif;
  }
  .tansu-photo{
    position:absolute;left:400px;top:0;width:449px;height:820px;
    background:linear-gradient(160deg,#5a1014 0%,#3a080b 45%,#1c0405 100%);
  }
  .craftsman-photo{
    position:absolute;left:0;top:545px;width:420px;height:573px;
    background:radial-gradient(ellipse at 45% 45%,var(--wood-light) 0%,#6a5242 35%,var(--wood-dark) 70%,#1a1210 100%);
  }
  .intro{
    position:absolute;left:40px;top:50px;height:470px;width:228px;
    writing-mode:vertical-rl;
    font-size:12.5px;line-height:1.9;letter-spacing:.06em;color:var(--paper);
  }
  .title{
    position:absolute;left:278px;top:40px;
    font-family:"Shippori Mincho B1",serif;font-weight:800;
    writing-mode:vertical-rl;color:var(--paper);font-size:102px;line-height:1;letter-spacing:.02em;
    text-shadow:0 2px 10px rgba(0,0,0,.55);
  }
  .motto{
    position:absolute;left:738px;top:495px;writing-mode:vertical-rl;
    font-family:"Shippori Mincho B1",serif;font-weight:500;font-size:25px;letter-spacing:.14em;color:var(--paper);
  }
  .signature{
    position:absolute;left:655px;top:720px;writing-mode:vertical-rl;
    font-size:14px;letter-spacing:.18em;color:var(--paper-soft);
  }
  .signature strong{font-weight:600;color:var(--paper);margin-top:14px;font-size:15px}
  .footer{
    position:absolute;left:0;top:1118px;width:849px;height:82px;background:var(--ink);
    display:flex;align-items:center;padding:0 24px 0 34px;
  }
  .workshop{display:flex;align-items:center;gap:12px;width:300px}
  .workshop__mark{width:30px;height:30px;border-radius:50%;background:var(--paper)}
  .workshop__name{font-family:"Shippori Mincho B1",serif;font-weight:500;font-size:24px;letter-spacing:.12em;color:var(--paper)}
  .contact{font-size:10px;line-height:1.6;color:var(--paper-soft);flex:1;letter-spacing:.02em}
  .qr-space{width:40px;height:40px;border:1px solid var(--paper-soft);background:#1c1414}
</style>
</head>
<body>
<main class="flyer">
  <div class="tansu-photo" role="img" aria-label="鉄金具が打たれた朱漆塗りの仙台箪笥の写真"></div>
  <div class="craftsman-photo" role="img" aria-label="作業台で鉋を手にする箪笥職人の写真"></div>

  <p class="intro">「仙台箪笥」は、江戸時代末期より仙台の地で作り続けられてきた伝統工芸品です。欅や杉の無垢材を吟味する木地づくり、幾度も塗り重ねる木地呂塗り、鉄を打ち出して文様を彫る金具づくり。そのすべての工程を職人の手しごとで仕上げることで、百年を超えて使い継がれる一棹が生まれます。近年は工場の機械で量産された品が同じ名で並ぶようになりました。けれども本物の箪笥は、使う人の暮らしとともに艶を増し、親から子へと受け継がれていくものです。柴崎庵は、手間を惜しまぬ本物のものづくりを、これからも愚直に守り続けます。</p>

  <h1 class="title">伝承の技、仙台箪笥</h1>

  <p class="motto">ほんものにこだわったものづくり</p>
  <p class="signature">仙台箪笥職人<strong>柴崎守</strong></p>

  <footer class="footer">
    <div class="workshop">
      <span class="workshop__mark"></span>
      <span class="workshop__name">仙台箪笥 柴崎庵</span>
    </div>
    <div class="contact">
      〒989-0000 仙台市杜ノ丘区架空町三丁目5-21<br>
      TEL 022-123-4567　FAX 022-123-4568<br>
      http://homepage5.example-host.jp/shibasakian/<br>
      Mail tokoharuwen@mailbox-demo.jp
    </div>
    <div class="qr-space" aria-label="ホームページQRコード掲載スペース"></div>
  </footer>
</main>
</body>
</html>
```